Basic Webdesign for a Financial Site

That's the design right now:

http://www.kurswellenplan.com

We want to keep the base design but make it look more modern and professional.

These are Designs we like:

https://www.boersmalde.de/
http://www.vindaro-shop.com/
http://hochkursmakler.de/
http://www.kolbrecoaching.com/

I use my own WordPress-Theme based on Chirper Bootstrap. I need a PSD and sliced Images (PNG) at the end. Thank you.

Financial

```html
<!DOCTYPE html>
<html lang="de">
<head>
<meta charset="utf-8">
<title>Renditeweg – Startseite</title>
<link href="https://fonts.googleapis.com/css2?family=Open+Sans:wght@400;600;700&family=Oswald:wght@400;500&display=swap" rel="stylesheet">
<style>
:root{
  --blue:#1a7fc4;
  --blue-dark:#0f5f9a;
  --blue-deep:#0b4a7a;
  --orange:#f0922b;
  --red:#e0362c;
  --lime:#c9e86b;
  --ink:#333;
  --muted:#7a7a7a;
  --line:#dcdcdc;
  --band:#eceff1;
  --footer:#2b2e33;
  --footer-dark:#1f2125;
  --white:#fff;
}
*{box-sizing:border-box;margin:0;padding:0}
html,body{width:773px;height:1200px;overflow:hidden}
body{font-family:"Open Sans",Arial,sans-serif;color:var(--ink);background:var(--white);font-size:7px;line-height:1.4}
.container{width:680px;margin:0 auto;position:relative}

/* header */
.site-header{height:48px;background:var(--white);border-bottom:1px solid var(--line)}
.site-header .container{width:760px;height:100%;display:flex;align-items:center;justify-content:space-between}
.brand{display:flex;align-items:center;gap:6px}
.brand-mark{width:20px;height:20px;background:var(--orange)}
.brand-name{font-family:"Oswald",sans-serif;font-weight:500;font-size:18px;color:var(--blue-deep);letter-spacing:.5px;text-transform:uppercase}
.header-right{display:flex;flex-direction:column;align-items:flex-end;gap:4px}
.account-links{display:flex;gap:12px;font-size:6px;font-weight:600;color:var(--ink)}
.account-links span::before{content:"";display:inline-block;width:5px;height:5px;background:var(--blue);border-radius:50%;margin-right:3px;vertical-align:middle}
.main-nav{display:flex;font-size:6.5px;font-weight:600;text-transform:uppercase}
.main-nav a{color:var(--ink);text-decoration:none;padding:6px 7px}
.main-nav a.active{background:var(--blue);color:var(--white);padding:10px 9px;margin-top:-8px}

/* hero */
.hero{height:274px;background:linear-gradient(180deg,#2a8ed3 0%,#1672b4 60%,#0f5f9a 100%);text-align:center;padding-top:12px}
.hero h1{font-weight:400;font-size:20px;line-height:28px;color:var(--lime)}
.hero-visual{width:340px;height:220px;margin:10px auto 0;border-radius:6px;background:linear-gradient(160deg,#3d4650,#1c232b)}

/* features */
.features{height:233px;padding-top:18px}
.features .container{display:flex;justify-content:space-between}
.feature{width:140px;text-align:center}
.feature-icon{width:48px;height:48px;border-radius:50%;margin:0 auto 8px;display:flex;align-items:center;justify-content:center;border:3px solid #e4e4e4}
.feature-icon.orange{background:var(--orange)}
.feature-icon.blue{background:var(--blue)}
.feature h3{font-size:8px;font-weight:700;color:var(--ink);margin-bottom:5px;text-transform:uppercase}
.feature p{font-size:5.5px;color:var(--muted);line-height:1.5}
.read-more{display:block;font-size:5.5px;color:var(--ink);margin-top:6px}

/* signup */
.signup-band{height:193px;background:var(--band);padding-top:44px}
.signup-box{width:360px;margin:0 auto;background:var(--white);padding:12px 18px;text-align:center;box-shadow:0 1px 2px rgba(0,0,0,.08)}
.signup-box h2{font-weight:400;font-size:13px;color:var(--ink);display:flex;align-items:center;justify-content:center;gap:6px}
.signup-form{display:flex;gap:5px;margin:9px 0 7px}
.signup-form span{flex:1;height:16px;border:1px solid var(--line);font-size:6px;color:#aaa;text-align:left;padding:3px 5px}
.signup-form .btn{flex:0 0 82px;background:var(--red);color:var(--white);border:none;font-weight:600;text-align:center}
.signup-note{font-size:6px;color:var(--muted)}

/* media */
.media{height:207px;padding-top:12px}
.media .container{display:flex;justify-content:space-between}
.section-title{font-size:8px;font-weight:700;text-transform:uppercase;text-align:center;border-bottom:1px solid var(--line);padding-bottom:4px;margin-bottom:8px;position:relative}
.videos{width:320px}
.pager{position:absolute;right:0;top:-2px;display:flex;gap:2px}
.pager i{width:9px;height:9px;background:var(--blue);display:block}
.pager i+i{background:#ccc}
.video-row{display:flex;gap:8px}
.video{flex:1}
.video-thumb{height:62px;background:linear-gradient(135deg,#3a6f9e,#1c3f60);display:flex;align-items:center;justify-content:center}
.video-caption{font-size:5.5px;color:var(--ink);margin-top:4px;display:flex;gap:4px}
.video-caption b{width:9px;height:9px;flex:0 0 9px;background:var(--blue);border-radius:50%}
.blog{width:330px}
.post{display:flex;gap:8px;margin-bottom:8px}
.post-date{width:24px;flex:0 0 24px;text-align:center;background:var(--blue);color:var(--white);font-size:8px;font-weight:700;line-height:1;padding:3px 0}
.post-date small{display:block;font-size:5px;font-weight:400;margin-top:2px}
.post-body{flex:1}
.post h4{font-size:6.5px;color:var(--blue);font-weight:600}
.post p{font-size:5px;color:var(--muted)}
.post .read-more{text-align:right;margin-top:0;font-size:5px}

/* social band */
.social-band{height:20px;background:var(--blue)}
.social-band .container{height:100%;display:flex;align-items:center;justify-content:space-between;font-size:5.5px;color:var(--white)}
.social-band .follow{font-size:6.5px;display:flex;align-items:center;gap:5px}
.social-band .follow i{width:9px;height:9px;border-radius:50%;background:var(--white);display:block}

/* footer */
.site-footer{height:199px;background:var(--footer);color:#c9c9c9;padding-top:14px}
.site-footer .container{display:flex;justify-content:space-between}
.footer-brand{width:150px}
.footer-brand .brand-name{color:var(--white);font-size:15px}
.contact{list-style:none;margin-top:12px;font-size:6px}
.contact li{display:flex;align-items:center;gap:5px;margin-bottom:8px}
.about{width:250px}
.site-footer h5{font-size:9px;color:var(--white);font-weight:600;margin-bottom:8px}
.about-body{display:flex;gap:8px}
.about-photo{width:52px;height:62px;flex:0 0 52px;background:linear-gradient(180deg,#7e8790,#4b535b)}
.about-body p{font-size:5.5px;line-height:1.6}
.footer-nav{width:140px}
.footer-nav ul{list-style:none;font-size:6px}
.footer-nav li{border-bottom:1px solid #3d4147;padding:3px 0}
.copyright{height:26px;background:var(--footer-dark);color:#9a9a9a;font-size:5.5px;text-align:center;line-height:26px}
</style>
</head>
<body>

<header class="site-header">
  <div class="container">
    <div class="brand"><span class="brand-mark"></span><span class="brand-name">Renditeweg</span></div>
    <div class="header-right">
      <div class="account-links"><span>SIGN UP</span><span>LOGIN</span></div>
      <nav class="main-nav">
        <a class="active">Startseite</a><a>Über uns</a><a>Buch</a><a>Blog</a><a>Produkte</a><a>Coaching</a><a>Notizbücher</a>
      </nav>
    </div>
  </div>
</header>

<section class="hero">
  <h1>So sichern sie sich an der Börse ein regelmäßiges Einkommen</h1>
  <div class="hero-visual" role="img" aria-label="Tablet, Laptop und Smartphone mit Börsencharts und Handelssoftware"></div>
</section>

<section class="features">
  <div class="container">
    <div class="feature">
      <div class="feature-icon orange"><svg width="22" height="16" viewBox="0 0 22 16"><path d="M1 2c4-1 7-1 10 1v13c-3-2-6-2-10-1z M21 2c-4-1-7-1-10 1v13c3-2 6-2 10-1z" fill="none" stroke="#fff" stroke-width="1.6"/></svg></div>
      <h3>Buch</h3>
      <p>Unser Buch zeigt Schritt für Schritt, wie Optionen funktionieren und wie Sie mit klaren Regeln ein stetiges Zusatzeinkommen aufbauen.</p>
      <span class="read-more">Read more</span>
    </div>
    <div class="feature">
      <div class="feature-icon blue"><svg width="20" height="20" viewBox="0 0 20 20"><path d="M10 1l8 4v10l-8 4-8-4V5z M2 5l8 4 8-4 M10 9v10" fill="none" stroke="#fff" stroke-width="1.6"/></svg></div>
      <h3>Produkte</h3>
      <p>Seminare, Videokurse und Werkzeuge für Trader, die ihre Strategien prüfen, verfeinern und im Depot sicher umsetzen wollen.</p>
      <span class="read-more">Read more</span>
    </div>
    <div class="feature">
      <div class="feature-icon orange"><svg width="20" height="18" viewBox="0 0 20 18"><path d="M2 2h16v10H8l-4 4v-4H2z" fill="none" stroke="#fff" stroke-width="1.6"/></svg></div>
      <h3>Blog</h3>
      <p>Aktuelle Marktkommentare, Analysen und Praxisbeispiele aus dem Handel – regelmäßig für Sie aufbereitet und leicht verständlich.</p>
      <span class="read-more">Read more</span>
    </div>
    <div class="feature">
      <div class="feature-icon blue"><svg width="22" height="16" viewBox="0 0 22 16"><path d="M11 1L1 6l10 5 10-5z M5 8v5c3 2 9 2 12 0V8" fill="none" stroke="#fff" stroke-width="1.6"/></svg></div>
      <h3>Coaching</h3>
      <p>Persönliche Begleitung im Einzelcoaching: wir besprechen Ihre Trades, Ihr Risiko und Ihren Plan für die nächsten Monate.</p>
      <span class="read-more">Read more</span>
    </div>
  </div>
</section>

<section class="signup-band">
  <div class="signup-box">
    <h2><svg width="14" height="14" viewBox="0 0 14 14"><circle cx="7" cy="7" r="6" fill="none" stroke="#333" stroke-width="1.2"/><path d="M4 5.5h.1M10 5.5h.1" stroke="#333" stroke-width="1.6" stroke-linecap="round"/><path d="M4 8.5c1.5 2 4.5 2 6 0" fill="none" stroke="#333" stroke-width="1.1"/></svg>Guess what! Signup us is free!</h2>
    <div class="signup-form"><span>Name</span><span>Password</span><span class="btn">Create an account</span></div>
    <p class="signup-note">Signup now and get 10% discount on your first contract!</p>
  </div>
</section>

<section class="media">
  <div class="container">
    <div class="videos">
      <div class="section-title">Our Videos<span class="pager"><i></i><i></i></span></div>
      <div class="video-row">
        <div class="video">
          <div class="video-thumb" role="img" aria-label="Vorschaubild Videokurs"><svg width="16" height="16" viewBox="0 0 16 16"><circle cx="8" cy="8" r="7.5" fill="#fff"/><path d="M6 4.5l5 3.5-5 3.5z" fill="#1a7fc4"/></svg></div>
          <div class="video-caption"><b></b>Ihr Einstieg in Optionen, Teil 1</div>
        </div>
        <div class="video">
          <div class="video-thumb" role="img" aria-label="Vorschaubild Videokurs"><svg width="16" height="16" viewBox="0 0 16 16"><circle cx="8" cy="8" r="7.5" fill="#fff"/><path d="M6 4.5l5 3.5-5 3.5z" fill="#1a7fc4"/></svg></div>
          <div class="video-caption"><b></b>Ihr Einstieg in Optionen, Teil 2</div>
        </div>
        <div class="video">
          <div class="video-thumb" role="img" aria-label="Vorschaubild Videokurs"><svg width="16" height="16" viewBox="0 0 16 16"><circle cx="8" cy="8" r="7.5" fill="#fff"/><path d="M6 4.5l5 3.5-5 3.5z" fill="#1a7fc4"/></svg></div>
          <div class="video-caption"><b></b>Ihr Einstieg in Optionen, Teil 3</div>
        </div>
      </div>
    </div>
    <div class="blog">
      <div class="section-title">From Our Blog</div>
      <article class="post">
        <div class="post-date">12<small>NOV</small></div>
        <div class="post-body"><h4>Allgemeiner Marktkommentar</h4><p>Die Märkte zeigen sich zum Wochenstart freundlich, die Volatilität sinkt weiter deutlich.</p><span class="read-more">Read more</span></div>
      </article>
      <article class="post">
        <div class="post-date">08<small>NOV</small></div>
        <div class="post-body"><h4>Allgemeiner Marktkommentar</h4><p>Nach den Zahlen der Notenbank bleibt der Ausblick stabil, wir halten unsere Positionen.</p><span class="read-more">Read more</span></div>
      </article>
      <article class="post">
        <div class="post-date">03<small>NOV</small></div>
        <div class="post-body"><h4>Allgemeiner Marktkommentar</h4><p>Ein ruhiger Handelstag mit engen Spannen bietet gute Chancen für neue Verkaufsoptionen.</p><span class="read-more">Read more</span></div>
      </article>
    </div>
  </div>
</section>

<section class="social-band">
  <div class="container">
    <span>Neu im Buch: Die besten Strategien für ruhige Märkte – jetzt vorbestellen und Bonuskapitel sichern.</span>
    <span class="follow"><i></i>Follow us on Chirper</span>
  </div>
</section>

<footer class="site-footer">
  <div class="container">
    <div class="footer-brand">
      <div class="brand"><span class="brand-mark"></span><span class="brand-name">Renditeweg</span></div>
      <ul class="contact">
        <li><svg width="7" height="9" viewBox="0 0 7 9"><path d="M3.5 0a3.3 3.3 0 013.3 3.3C6.8 5.5 3.5 9 3.5 9S.2 5.5.2 3.3A3.3 3.3 0 013.5 0z" fill="#c9c9c9"/></svg>Lindenweg 14, 60311 Frankfurt</li>
        <li><svg width="8" height="8" viewBox="0 0 8 8"><path d="M1 0h2l1 2-1 1c.5 1 1 1.5 2 2l1-1 2 1v2c-4 0-7-3-7-7z" fill="#c9c9c9"/></svg>+49 69 4471 2208</li>
        <li><svg width="8" height="6" viewBox="0 0 8 6"><rect width="8" height="6" fill="#c9c9c9"/><path d="M0 0l4 3 4-3" fill="none" stroke="#2b2e33" stroke-width=".8"/></svg>info@renditeweg.de</li>
      </ul>
    </div>
    <div class="about">
      <h5>Über uns</h5>
      <div class="about-body">
        <div class="about-photo" role="img" aria-label="Porträtfoto des Autors"></div>
        <p>Seit über zehn Jahren handeln wir Optionen an internationalen Börsen. Unser Ziel ist es, Privatanlegern verständliche Strategien an die Hand zu geben, mit denen sie ihr Kapital schützen und ein planbares monatliches Einkommen erzielen können.</p>
      </div>
    </div>
    <nav class="footer-nav">
      <h5>Navigate</h5>
      <ul><li>Startseite</li><li>Über uns</li><li>Buch</li><li>Blog</li><li>Produkte</li><li>Coaching</li><li>Notizbücher</li></ul>
    </nav>
  </div>
</footer>
<div class="copyright">© 2013 Renditeweg · All Rights Reserved</div>

</body>
</html>
```